We are looking for a new website design for our SEO WEB Development Company. The URL is www.brightlanterndigital.example

We want it to be a more powerful representation of what we do. We are also looking for a number of designers that we will give continuous business to every month. The persons design we choose will also get a proposal to complete 4 - 6 new designs for us every month for our clients.

Be creative as you can in your design submissions. We really want to stand out!

Just to give you an idea of what we like look at this site: http://www.corvexsiteworks.example/

```html
<!DOCTYPE html>
<html lang="en">
<head>
<meta charset="utf-8">
<title>Lantern Interactive Group</title>
<link rel="stylesheet" href="https://fonts.googleapis.com/css2?family=Arimo:wght@400;700&family=Questrial&family=PT+Sans:wght@400;700&display=swap">
<style>
:root{
  --orange:#cc6300;
  --orange-light:#e07a10;
  --orange-text:#c25a00;
  --ink:#3c3c52;
  --navy:#1f3a6b;
  --body:#4a4a4a;
  --paper:#ebe9e4;
  --panel:#ffffff;
  --dark:#1f2026;
  --rule:#cfcfcf;
}
*{margin:0;padding:0;box-sizing:border-box}
html,body{width:1200px;height:1153px;overflow:hidden}
body{position:relative;background:var(--paper);font-family:"Arimo",Arial,sans-serif;color:var(--body)}
.abs{position:absolute}

.top-line{left:0;top:0;width:1200px;height:2px;background:var(--orange)}
.header{left:0;top:2px;width:1200px;height:140px;background:#fff}
.brand{left:189px;top:52px;display:flex;align-items:center;gap:10px;font-family:"Questrial",sans-serif;font-size:26px;color:var(--orange-text)}
.brand-mark{width:22px;height:22px;background:var(--orange-text)}
.call{right:183px;top:54px;font-family:"Questrial",sans-serif;font-size:24px;color:var(--orange-light)}
.call strong{color:var(--ink);font-size:30px;font-weight:700;font-family:"Arimo",sans-serif;letter-spacing:.5px}

.nav{left:436px;top:115px;width:581px;height:28px;background:linear-gradient(#4a4c5a,#2a2b34);border-radius:6px 6px 0 0;display:flex;align-items:center;justify-content:space-around;padding:0 6px;font-family:"Questrial",sans-serif;font-size:13.5px;color:#e6e6e6}
.nav .sep{width:1px;height:14px;background:#666}
.nav .active{font-weight:700;font-family:"Arimo",sans-serif;color:#fff}
.nav-bar{left:0;top:142px;width:1200px;height:6px;background:var(--dark)}

.band-top{left:0;top:148px;width:1200px;height:218px;background:linear-gradient(var(--orange),#d06a08)}
.band-bottom{left:0;top:895px;width:1200px;height:228px;background:linear-gradient(var(--orange-light),var(--orange))}
.copyright-bar{left:0;top:1123px;width:1200px;height:30px;background:linear-gradient(#3a3a3a,#1b1b1b);color:#e0e0e0;font-size:11px;text-align:center;line-height:30px;letter-spacing:.5px}

.hero-shape{left:189px;top:157px}
.hero-photo{left:208px;top:188px;width:394px;height:178px;border:1px solid #bbb;background:linear-gradient(135deg,#e4e6ea,#b8a890 45%,#9aa3ad 70%,#e8e8ea)}
.hero-title{left:627px;top:186px;font-family:"Questrial",sans-serif;font-size:31px;color:var(--orange-light)}
.hero-text{left:626px;top:239px;width:370px;font-size:13px;line-height:17px;color:#444}
.quote-btn{left:859px;top:350px;width:127px;height:34px;border-radius:10px;background:linear-gradient(#f6931e,#d96a00);border:2px solid #fff;box-shadow:0 1px 3px rgba(0,0,0,.3);color:#fff;font-family:"Questrial",sans-serif;font-size:19px;text-align:center;line-height:30px}
.follow{left:855px;top:415px;display:flex;align-items:center;gap:6px;font-size:11px;font-weight:700;color:#222;letter-spacing:.8px}
.follow .social{width:21px;height:21px;border-radius:3px;margin-left:2px}

.content{left:189px;top:446px;width:828px;height:502px;background:var(--panel);border-radius:0 0 8px 8px}
.welcome-title{left:208px;top:469px;font-family:"PT Sans",sans-serif;font-weight:700;font-size:21px;color:var(--ink);letter-spacing:.5px}
.welcome{left:208px;top:511px;width:497px;font-size:11.4px;line-height:19px;text-align:justify}
.welcome p{margin-bottom:19px}
.welcome b{color:var(--orange-text)}
.divider{left:731px;top:472px;height:452px;border-left:1px dotted #bbb}

.expert-title{left:760px;top:467px;font-family:"PT Sans",sans-serif;font-weight:700;font-size:17px;color:var(--ink);letter-spacing:.5px}
.expert-intro{left:761px;top:497px;width:240px;font-size:12.5px;line-height:21px;color:var(--navy)}
.expert-list{left:761px;top:564px;list-style:none;font-size:12.5px;color:var(--navy)}
.expert-list li{display:flex;align-items:center;height:24.7px;gap:14px}

.contact{left:759px;top:724px;width:230px;height:209px;border:1px solid #ddd;border-radius:4px;background:linear-gradient(#f1f1f1,#fff 40%)}
.contact h3{position:absolute;left:10px;top:10px;font-family:"PT Sans",sans-serif;font-size:18px;color:var(--ink)}
.field{position:absolute;left:9px;width:207px;height:19px;border:1px solid #bbb;background:#fff;font-size:10.5px;color:#999;padding:2px 5px}
.submit{position:absolute;right:14px;bottom:8px;font-family:"PT Sans",sans-serif;font-weight:700;font-size:14px;color:var(--ink)}

.foot-col{top:962px;color:#fff;font-size:11.5px}
.foot-col h4{font-weight:700;font-size:11.5px;height:23px;margin-bottom:0}
.foot-col ul{list-style:none;margin-top:13px}
.foot-col li{line-height:19px;color:#fde9d6}
.foot-rule{left:227px;top:985px;width:744px;height:1px;background:#e8924a}
</style>
</head>
<body>
<div class="abs top-line"></div>
<header class="abs header"></header>
<div class="abs brand"><span class="brand-mark"></span>Lantern Interactive Group</div>
<div class="abs call">Call Us: <strong>555-014-7720</strong></div>
<nav class="abs nav">
  <span class="active">HOME</span><span class="sep"></span>
  <span>CREATIVE DESIGN</span><span class="sep"></span>
  <span>WEBSITE DESIGN</span><span class="sep"></span>
  <span>INTERNET MARKETING</span><span class="sep"></span>
  <span>IT CONSULTING</span>
</nav>
<div class="abs nav-bar"></div>

<div class="abs band-top"></div>
<div class="abs band-bottom"></div>

<svg class="abs hero-shape" width="828" height="268" viewBox="0 0 828 268" aria-hidden="true">
  <defs>
    <linearGradient id="heroFill" x1="0" y1="0" x2="0" y2="1">
      <stop offset="0" stop-color="#ffffff"/>
      <stop offset="1" stop-color="#dcdcdc"/>
    </linearGradient>
  </defs>
  <path d="M10,0 H818 Q828,0 828,10 V240 H200 C170,240 165,266 140,266 H10 Q0,266 0,256 V10 Q0,0 10,0 Z" fill="url(#heroFill)" stroke="#fff" stroke-width="3"/>
</svg>
<div class="abs hero-photo" role="img" aria-label="Team of five business people in light suits standing around a globe"></div>
<h1 class="abs hero-title" style="font-weight:400">Best Interactive Group</h1>
<p class="abs hero-text">Lorem Ipsum is simply dummy text of the printing and typesetting industry. Lorem Ipsum has been the industry's standard dummy text ever since the 1500s, when an Lorem Ipsum is simply dummy text of the printing &nbsp;the 1500s, when an simply dummy text of the printing &nbsp;the 1500s.</p>
<div class="abs quote-btn">Get a Quote</div>
<div class="abs follow">follow us on:
  <span class="social" style="background:#3b5a9a"></span>
  <span class="social" style="background:#3a8fc8"></span>
  <span class="social" style="background:#7fcbe0"></span>
</div>

<main class="abs content"></main>
<h2 class="abs welcome-title">WELCOME TO OUR WEBSITE</h2>
<div class="abs welcome">
  <p><b>Lantern Interactive Group is a leading Dallas Web Site Design,</b> Publishing and Internet Marketing Firm. Our Dallas Texas based Website Design and Internet Marketing experts are some of the best in the industry!</p>
  <p><b>Lantern Interactive Web is a full-service Dallas based Advertising</b> Agency comprised of experienced advertising and marketing professionals that provide clients with a clear and distinct voice in the marketplace. Web Site Design and Internet Marketing experts at our Dallas location specialize in developing Online Marketing Strategies, Search Engine Marketing and Optimization (SEO), Pay Per Click , Web Site Design and Development, and Online Reputation Management.</p>
  <p><b>Lantern Interactive Publishing provides full-service custom</b> publishing and consulting services for magazines, newsletters, blogs and web sites. We are the complete interactive publishing arm for your organization. Our services include: Strategic Planning and Computer Modeling;</p>
  <p>Art Direction and Design; Production Services; Circulation Marketing and Management; Subscription Fulfillment Management; Advertising Sales Management; Web Site and Digital Magazine Design and Management; and Video Streaming Services.</p>
</div>
<div class="abs divider"></div>

<h2 class="abs expert-title">WE ARE EXPERT IN</h2>
<p class="abs expert-intro">Lorem Ipsum is simply dummy text of the printing and typesetting industry.</p>
<ul class="abs expert-list">
  <li><svg width="16" height="14" viewBox="0 0 16 14"><path d="M1,7 L6,12 L15,1" fill="none" stroke="#e07a10" stroke-width="3"/></svg>Search Engine Marketing</li>
  <li><svg width="16" height="14" viewBox="0 0 16 14"><path d="M1,7 L6,12 L15,1" fill="none" stroke="#e07a10" stroke-width="3"/></svg>Optimization (SEO)</li>
  <li><svg width="16" height="14" viewBox="0 0 16 14"><path d="M1,7 L6,12 L15,1" fill="none" stroke="#e07a10" stroke-width="3"/></svg>Pay Per Click</li>
  <li><svg width="16" height="14" viewBox="0 0 16 14"><path d="M1,7 L6,12 L15,1" fill="none" stroke="#e07a10" stroke-width="3"/></svg>Web Site Design</li>
  <li><svg width="16" height="14" viewBox="0 0 16 14"><path d="M1,7 L6,12 L15,1" fill="none" stroke="#e07a10" stroke-width="3"/></svg>Web Development</li>
  <li><svg width="16" height="14" viewBox="0 0 16 14"><path d="M1,7 L6,12 L15,1" fill="none" stroke="#e07a10" stroke-width="3"/></svg>Online Reputation Management</li>
</ul>

<form class="abs contact">
  <h3>Contact Us:</h3>
  <div class="field" style="top:38px">Name:</div>
  <div class="field" style="top:61px">Email:</div>
  <div class="field" style="top:84px">Phone:</div>
  <div class="field" style="top:106px;height:67px">Message:</div>
  <span class="submit">Submit</span>
</form>

<div class="abs foot-rule"></div>
<div class="abs foot-col" style="left:227px"><h4>CREATIVE DESIGN</h4><ul><li>Creative Advertising Print</li><li>Design Corporate Identity</li><li>Packaging</li></ul></div>
<div class="abs foot-col" style="left:429px"><h4>INTERNET MARKETING</h4><ul><li>Search Engine</li><li>Optimization Pay-per-Click</li><li>Campaign Consulting</li><li>Email Marketing SEO</li><li>Copywriting Reputation</li><li>Management</li></ul></div>
<div class="abs foot-col" style="left:656px"><h4>WEBSITE DESIGN</h4><ul><li>Web Design E-commerce</li><li>Multimedia Web</li><li>Application Development</li></ul></div>
<div class="abs foot-col" style="left:857px"><h4>LANTERN INTERACTIVE</h4><ul><li>About Us</li><li>Our Work</li><li>Contact Us</li></ul></div>

<footer class="abs copyright-bar">Copyright © 2011 Lantern Interactive Group. All Rights Reserved</footer>
</body>
</html>
```